Byte Lantern Website

Design and implement (fully coded and ready to launch) website for a professional services company - please see the documents attached and send us an email if there are any questions
Target Market(s)
Market to potential clients about the services we offer and be able to reach us for any consulting opportunities
Industry/Entity Type
Professional Service
Coding
Coded - Design and coding required
Number of Pages Required
3 page
Requirements
Must have
- Single page website design that is SEO optimized
Blog Post
Contact US page
Cool images/ logos for the service offering - not fill the website with text/content
Must be professional looking website
Coded website should also look great on different screens - mobile, tablets etc
Nice to have
- Choose easy neutral colors that compliment the logo colors. Having said that don't use every color in the logo for the website design.
Should not have
- Too many colors and several various different fonts

```html
<!DOCTYPE html>
<html lang="en">
<head>
<meta charset="utf-8">
<title>Byte Lantern LLC</title>
<link href="https://fonts.googleapis.com/css2?family=Michroma&family=Roboto:wght@400;500;700&display=swap" rel="stylesheet">
<style>
:root{
  --blue:#0d4aa6;
  --blue-dark:#0c3f98;
  --navy:#1b2a4a;
  --orange:#f26a1b;
  --red:#e8341c;
  --purple:#8e3ea8;
  --mid-blue:#2670c2;
  --ink:#1c1c1c;
  --text:#555b66;
  --lavender:#f3f4fc;
  --line:#d9dcea;
  --ghost:#eceef7;
}
*{box-sizing:border-box;margin:0;padding:0}
html,body{width:1200px;height:3828px;overflow:hidden}
body{position:relative;font-family:'Roboto',sans-serif;color:var(--text);background:#fff}
.abs{position:absolute}
.head{font-family:'Michroma',sans-serif;font-weight:400;white-space:nowrap}
.section-title{position:absolute;left:0;width:1200px;text-align:center;font-family:'Michroma',sans-serif;font-size:40px;letter-spacing:1px;color:var(--ink);white-space:nowrap}
.section-title span{color:var(--blue)}
.section-ghost{position:absolute;left:0;width:1200px;text-align:center;font-family:'Michroma',sans-serif;font-size:56px;color:var(--ghost);letter-spacing:2px;white-space:nowrap}
.rule{position:absolute;left:541px;width:118px;height:2px;background:var(--blue)}

/* hero */
.hero-art{left:555px;top:30px;width:615px;height:580px;border-radius:40px;background:radial-gradient(circle at 50% 45%,#cfe0fa 0%,#e6eefc 45%,#fff 75%);z-index:0}
.hero-text{z-index:2}
.brand{left:88px;top:42px;width:300px;text-align:center}
.brand-mark{display:block;margin:0 auto 8px;width:36px;height:36px;border-radius:50%;background:var(--red)}
.brand-name{font-family:'Michroma',sans-serif;font-size:21px;color:var(--ink);white-space:nowrap}
.brand-llc{display:block;text-align:right;font-family:'Michroma',sans-serif;font-size:11px;color:var(--ink)}
.hero-title{left:88px;top:308px;font-size:41px;color:var(--blue)}
.hero-sub{left:88px;top:368px;font-size:29px;color:var(--ink)}
.hero-sub small{font-size:15px}
.hero-copy{left:88px;top:424px;width:420px;font-size:13.5px;line-height:21px;color:#444}
.btn{position:absolute;height:50px;border-radius:4px;color:#fff;font-size:15px;display:flex;align-items:center;justify-content:center;gap:8px;z-index:2}
.btn-red{left:90px;top:510px;width:170px;background:var(--red)}
.btn-blue{left:273px;top:510px;width:170px;background:var(--blue)}

/* services */
.svc-num{font-family:'Roboto',sans-serif;font-weight:700;font-size:110px}
.svc-h{font-family:'Roboto',sans-serif;font-weight:500;font-size:26px;color:var(--ink)}
.svc-p{font-size:13.5px;line-height:21px;color:#555;width:440px}
.svc-link{font-size:14.5px;font-weight:500}

/* team */
.team-bg{left:0;top:1594px;width:1200px;height:756px;background:var(--lavender)}
.team-copy{left:170px;top:1786px;width:860px;text-align:center;font-size:13.5px;line-height:21px;color:#555}
.member-name{font-family:'Michroma',sans-serif;font-size:19px;color:var(--ink);width:300px;text-align:center;white-space:nowrap}
.member-role{font-size:13px;font-weight:700;color:var(--blue);width:300px;text-align:center}
.social{display:flex;gap:14px;width:300px;justify-content:center}
.social i{width:34px;height:34px;border-radius:50%;border:1.5px solid var(--blue);display:flex;align-items:center;justify-content:center}
.social i::after{content:"";width:6px;height:6px;border-radius:50%;background:var(--blue)}

/* blog */
.card{position:absolute;top:2558px;width:320px;height:502px;border:1px solid #e6e6ee;background:#fff}
.card-img{height:280px}
.card-date{position:absolute;right:10px;top:248px;width:80px;height:40px;background:#fff;text-align:center;font-size:11px;line-height:14px;color:#333;padding-top:6px}
.card-meta{margin:22px 0 0 24px;font-size:13.5px;color:var(--blue);display:flex;gap:16px}
.card-meta b{font-weight:400}
.card-title{margin:10px 24px 0;font-size:17.5px;line-height:24px;color:var(--ink);font-weight:400}
.card-copy{margin:14px 24px 0;font-size:13.5px;line-height:21px;color:#666}
.card-btn{position:absolute;left:23px;top:446px;width:119px;height:39px;background:var(--blue);color:#fff;font-size:14px;display:flex;align-items:center;justify-content:center;border-radius:2px}

/* tech */
.tech{position:absolute;top:3325px;width:88px;height:88px;border-radius:50%;background:#fff;box-shadow:0 4px 14px rgba(30,40,90,.12);display:flex;align-items:center;justify-content:center;font-size:11px;font-weight:700;color:var(--blue)}
.tech::before{content:"";width:26px;height:26px;border-radius:50%;background:var(--ghost);position:absolute}
.tech span{position:relative}

/* footer */
.footer{left:0;top:3490px;width:1200px;height:338px;background:var(--blue-dark)}
.foot-h{font-family:'Michroma',sans-serif;font-size:17px;color:#fff;white-space:nowrap}
.foot-list{list-style:none;font-size:14px;color:#fff;line-height:26.5px}
.foot-list li::before{content:"";display:inline-block;width:4px;height:4px;border-radius:50%;background:#8fb0e6;margin-right:10px;vertical-align:middle}
.foot-social{font-size:13px;color:#fff}
.foot-social div{display:flex;align-items:center;gap:12px;height:37px}
.foot-social i,.contact i{width:24px;height:24px;border-radius:50%;background:rgba(255,255,255,.18);display:inline-block;flex:none}
.contact{font-size:13.5px;color:#fff;width:220px}
.contact div{display:flex;gap:12px;margin-bottom:12px}
.contact small{display:block;font-size:11.5px;color:#dbe6ff;margin-top:2px;line-height:14px}
.foot-brand{left:100px;top:3600px;width:295px;text-align:center}
.foot-brand-name{font-family:'Michroma',sans-serif;font-size:22px;color:#fff;white-space:nowrap}
.copy{left:0;top:3795px;width:1200px;text-align:center;font-size:13.5px;color:#fff}
</style>
</head>
<body>

<!-- HERO -->
<svg class="abs" style="left:0;top:0" width="520" height="670" viewBox="0 0 520 670" aria-hidden="true">
  <path d="M0 0 H70 C140 60 110 120 250 110 C420 100 470 300 480 470 C490 600 350 660 200 655 C110 652 40 640 0 650 Z" fill="#f1f2fb"/>
</svg>
<div class="abs hero-art" role="img" aria-label="Isometric illustration of people working with servers, cloud storage and a laptop"></div>
<div class="abs brand hero-text">
  <span class="brand-mark"></span>
  <div class="brand-name">BYTE LANTERN</div>
  <span class="brand-llc">LLC</span>
</div>
<h1 class="abs head hero-title hero-text">WELCOME TO</h1>
<div class="abs head hero-sub hero-text">BYTE LANTERN <small>LLC</small></div>
<p class="abs hero-copy hero-text">Byte Lantern provides end to end services in architecture, design &amp; development of Data Platforms, Analytic workloads, Data Engineering, Cloud Engineering</p>
<a class="btn btn-red">Read More <svg width="24" height="8"><path d="M0 4H22M18 1l4 3-4 3" stroke="#fff" fill="none"/></svg></a>
<a class="btn btn-blue">Get a Quote <svg width="24" height="8"><path d="M0 4H22M18 1l4 3-4 3" stroke="#fff" fill="none"/></svg></a>

<!-- SERVICES -->
<div class="section-ghost" style="top:698px">SERVICES</div>
<h2 class="section-title" style="top:736px"><span>OUR</span> SERVICES</h2>
<div class="rule" style="top:800px"></div>
<svg class="abs" style="left:1040px;top:800px" width="160" height="300" aria-hidden="true"><path d="M160 10 L60 90 L60 200 L160 280" stroke="#f1f2fb" stroke-width="40" fill="none"/></svg>

<svg class="abs" style="left:0;top:840px" width="1200" height="700" aria-hidden="true">
  <line x1="600" y1="112" x2="600" y2="584" stroke="#b9c2dd" stroke-dasharray="3 3"/>
  <line x1="472" y1="112" x2="600" y2="112" stroke="#b9c2dd" stroke-dasharray="3 3"/>
  <line x1="600" y1="341" x2="728" y2="341" stroke="#b9c2dd" stroke-dasharray="3 3"/>
  <line x1="472" y1="582" x2="600" y2="582" stroke="#b9c2dd" stroke-dasharray="3 3"/>
  <circle cx="600" cy="112" r="8" fill="var(--orange)"/>
  <circle cx="600" cy="341" r="8" fill="var(--purple)"/>
  <circle cx="600" cy="582" r="8" fill="var(--mid-blue)"/>
  <g>
    <circle cx="370" cy="112" r="101" fill="#fff" stroke="#e2e6f2" stroke-width="2"/>
    <circle cx="370" cy="112" r="84" fill="none" stroke="#c5d1ea" stroke-width="2"/>
    <circle cx="370" cy="112" r="72" fill="var(--orange)"/>
    <path d="M335 115 a18 18 0 0 1 8-32 a24 24 0 0 1 44-4 a18 18 0 0 1 4 36 Z" fill="none" stroke="#fff" stroke-width="3"/>
    <path d="M352 115v18M364 115v24M376 115v24M388 115v18" stroke="#fff" stroke-width="3"/>
  </g>
  <g>
    <circle cx="840" cy="341" r="101" fill="#fff" stroke="#e2e6f2" stroke-width="2"/>
    <circle cx="840" cy="341" r="84" fill="none" stroke="#c5d1ea" stroke-width="2"/>
    <circle cx="840" cy="341" r="72" fill="var(--purple)"/>
    <ellipse cx="832" cy="312" rx="28" ry="9" fill="none" stroke="#fff" stroke-width="3"/>
    <path d="M804 312v46c0 5 13 9 28 9M860 312v22M804 328c0 5 13 9 28 9M804 344c0 5 13 9 28 9" fill="none" stroke="#fff" stroke-width="3"/>
    <circle cx="856" cy="345" r="9" fill="none" stroke="#fff" stroke-width="3"/>
    <path d="M840 372c2-12 30-12 32 0" fill="none" stroke="#fff" stroke-width="3"/>
  </g>
  <g>
    <circle cx="370" cy="582" r="101" fill="#fff" stroke="#e2e6f2" stroke-width="2"/>
    <circle cx="370" cy="582" r="84" fill="none" stroke="#c5d1ea" stroke-width="2"/>
    <circle cx="370" cy="582" r="72" fill="var(--mid-blue)"/>
    <path d="M338 570 a16 16 0 0 1 8-28 a22 22 0 0 1 40-2 a16 16 0 0 1 2 30 Z" fill="none" stroke="#fff" stroke-width="3"/>
    <circle cx="370" cy="604" r="12" fill="none" stroke="#fff" stroke-width="3" stroke-dasharray="5 3"/>
    <circle cx="370" cy="604" r="4" fill="#fff"/>
  </g>
</svg>

<div class="abs svc-num" style="left:118px;top:885px;color:#fcebe1">01</div>
<div class="abs svc-h" style="left:665px;top:880px">PLATFORM ARCHITECTURE</div>
<p class="abs svc-p" style="left:666px;top:928px">Byte Lantern works very closely with clients, product managers to understand the scope of the requirements, discuss myriad of technologies choices available...</p>
<div class="abs svc-link" style="left:666px;top:1002px;color:var(--orange)">Learn More &rarr;</div>

<div class="abs svc-num" style="left:952px;top:1112px;color:#f5ecf6">02</div>
<div class="abs svc-h" style="left:126px;top:1110px">DATA ENGINEERING</div>
<p class="abs svc-p" style="left:126px;top:1158px">Byte Lantern employs the latest proven technologies, best practices, industry standards in building the Data Lakes that has become the business standard in any Industry...</p>
<div class="abs svc-link" style="left:126px;top:1232px;color:var(--purple)">Learn More &rarr;</div>

<div class="abs svc-num" style="left:118px;top:1355px;color:#e9eff9">03</div>
<div class="abs svc-h" style="left:665px;top:1352px">CLOUD DEVELOPMENTS</div>
<p class="abs svc-p" style="left:666px;top:1400px">There are numerous technology options, tools, cloud services that can be utilized but guiding through to make the right decision will save our clients...</p>
<div class="abs svc-link" style="left:666px;top:1474px;color:var(--mid-blue)">Learn More &rarr;</div>

<!-- TEAM -->
<div class="abs team-bg"></div>
<div class="section-ghost" style="top:1655px;color:#e6e8f4">OUR TEAM</div>
<h2 class="section-title" style="top:1694px"><span>COMPANY</span> MEMBERS</h2>
<div class="rule" style="top:1760px"></div>
<p class="abs team-copy">Arun manages all the client interactions and engineering team at Byte Lantern. Arun has over 15 years of experience in the technology before he founded Byte Lantern. He managed development of large scale enterprise wide, high performance, scalable, real-time software solutions in Tele-communications, Gaming, Finance, and Insurance Industries.</p>

<svg class="abs" style="left:0;top:1880px" width="1200" height="300" aria-hidden="true">
  <g fill="none" stroke="#dcd0e6" stroke-width="2">
    <circle cx="268" cy="145" r="140"/><circle cx="606" cy="145" r="140"/><circle cx="944" cy="145" r="140"/>
  </g>
  <circle cx="268" cy="145" r="117" fill="none" stroke="var(--orange)" stroke-width="2"/>
  <circle cx="606" cy="145" r="117" fill="none" stroke="var(--purple)" stroke-width="2"/>
  <circle cx="944" cy="145" r="117" fill="none" stroke="var(--mid-blue)" stroke-width="2"/>
  <circle cx="398" cy="200" r="10" fill="none" stroke="#e9a7a0" stroke-width="2"/>
  <circle cx="734" cy="200" r="10" fill="none" stroke="#e9a7a0" stroke-width="2"/>
  <circle cx="1072" cy="200" r="10" fill="none" stroke="#e9a7a0" stroke-width="2"/>
</svg>
<div class="abs" style="left:151px;top:1908px;width:234px;height:234px;border-radius:50%;background:linear-gradient(150deg,#e8edf2,#a9b8c8)" role="img" aria-label="Portrait photo of team member"></div>
<div class="abs" style="left:489px;top:1908px;width:234px;height:234px;border-radius:50%;background:linear-gradient(150deg,#4e5a52,#d9d6cf)" role="img" aria-label="Portrait photo of team member on the phone"></div>
<div class="abs" style="left:827px;top:1908px;width:234px;height:234px;border-radius:50%;background:linear-gradient(150deg,#f1f3f5,#c7ced6)" role="img" aria-label="Portrait photo of team member"></div>
<svg class="abs" style="left:0;top:1880px" width="1200" height="300" aria-hidden="true">
  <g><circle cx="145" cy="220" r="42" fill="#fff"/><circle cx="145" cy="220" r="36" fill="var(--orange)"/>
    <path d="M128 236l32-32M132 204l28 28" stroke="#fff" stroke-width="3"/></g>
  <g><circle cx="482" cy="220" r="42" fill="#fff"/><circle cx="482" cy="220" r="36" fill="var(--purple)"/>
    <rect x="466" y="208" width="32" height="20" rx="2" fill="none" stroke="#fff" stroke-width="3"/><path d="M462 234h40" stroke="#fff" stroke-width="3"/></g>
  <g><circle cx="820" cy="220" r="42" fill="#fff"/><circle cx="820" cy="220" r="36" fill="var(--mid-blue)"/>
    <path d="M804 214h8l16-10v32l-16-10h-8z" fill="none" stroke="#fff" stroke-width="3"/><path d="M834 212l6-4M834 220h8M834 228l6 4" stroke="#fff" stroke-width="3"/></g>
</svg>

<div class="abs member-name" style="left:118px;top:2182px">ARUN KESSLER</div>
<div class="abs member-role" style="left:118px;top:2213px">FOUNDER</div>
<div class="abs social" style="left:118px;top:2242px"><i></i><i></i><i></i><i></i></div>
<div class="abs member-name" style="left:456px;top:2182px">ARUN KESSLER</div>
<div class="abs member-role" style="left:456px;top:2213px">FOUNDER</div>
<div class="abs social" style="left:456px;top:2242px"><i></i><i></i><i></i><i></i></div>
<div class="abs member-name" style="left:794px;top:2182px">ARUN KESSLER</div>
<div class="abs member-role" style="left:794px;top:2213px">FOUNDER</div>
<div class="abs social" style="left:794px;top:2242px"><i></i><i></i><i></i><i></i></div>

<!-- BLOG -->
<div class="section-ghost" style="top:2415px">OUR BLOG</div>
<h2 class="section-title" style="top:2452px"><span>LATEST</span> PROJECT</h2>
<div class="rule" style="top:2518px"></div>

<article class="card" style="left:90px">
  <div class="card-img" role="img" aria-label="Photo of a woman working on a laptop" style="background:linear-gradient(160deg,#7fa0a8,#e6c7b8)"></div>
  <div class="card-date">01<br>November</div>
  <div class="card-meta"><b>&#9679; By Admin</b><b>&#9632; 03 Comments</b></div>
  <h3 class="card-title">Lorem Ipsum is simply dummy text of the printing</h3>
  <p class="card-copy">Lorem Ipsum is simply dummy text of the printing &amp; typesetting industry.</p>
  <a class="card-btn">Read More</a>
</article>
<article class="card" style="left:441px">
  <div class="card-img" role="img" aria-label="Photo of a man smiling at a laptop" style="background:linear-gradient(160deg,#d7dde0,#b49aa6)"></div>
  <div class="card-date">01<br>November</div>
  <div class="card-meta"><b>&#9679; By Admin</b><b>&#9632; 03 Comments</b></div>
  <h3 class="card-title">Lorem Ipsum is simply dummy text of the printing</h3>
  <p class="card-copy">Lorem Ipsum is simply dummy text of the printing &amp; typesetting industry.</p>
  <a class="card-btn">Read More</a>
</article>
<article class="card" style="left:791px">
  <div class="card-img" role="img" aria-label="Photo of a businessman with coffee at a laptop" style="background:linear-gradient(160deg,#5e6770,#c9ced3)"></div>
  <div class="card-date">01<br>November</div>
  <div class="card-meta"><b>&#9679; By Admin</b><b>&#9632; 03 Comments</b></div>
  <h3 class="card-title">Lorem Ipsum is simply dummy text of the printing</h3>
  <p class="card-copy">Lorem Ipsum is simply dummy text of the printing &amp; typesetting industry.</p>
  <a class="card-btn">Read More</a>
</article>

<div class="abs" style="left:90px;top:3130px;width:1020px;height:1px;background:var(--line)"></div>

<!-- TECHNOLOGY -->
<div class="section-ghost" style="top:3205px">TECHNOLOGY</div>
<h2 class="section-title" style="top:3240px"><span>TECHNOLOGY</span> EXPERTISE</h2>
<div class="rule" style="top:3300px"></div>
<div class="tech" style="left:96px"></div>
<div class="tech" style="left:199px"></div>
<div class="tech" style="left:302px"></div>
<div class="tech" style="left:405px"><span>Flintware</span></div>
<div class="tech" style="left:508px"></div>
<div class="tech" style="left:611px"></div>
<div class="tech" style="left:714px"><span>Queuery</span></div>
<div class="tech" style="left:817px"></div>
<div class="tech" style="left:920px"><span>Skyloft</span></div>
<div class="tech" style="left:1023px"></div>

<!-- FOOTER -->
<footer class="abs footer"></footer>
<div class="abs" style="left:0;top:3490px;width:1200px;height:338px;background:radial-gradient(ellipse at 65% 45%,rgba(255,255,255,.07),transparent 60%)" role="img" aria-label="Faint dotted world map backdrop"></div>
<div class="abs foot-brand">
  <span style="display:block;margin:0 auto 10px;width:36px;height:36px;border-radius:50%;background:#fff"></span>
  <div class="foot-brand-name">BYTE LANTERN</div>
  <div style="text-align:right;font-family:'Michroma',sans-serif;font-size:11px;color:#fff">LLC</div>
</div>

<div class="abs foot-h" style="left:460px;top:3545px">USEFUL LINKS</div>
<ul class="abs foot-list" style="left:460px;top:3585px">
  <li>Home</li><li>Services</li><li>Team</li><li>Project</li><li>Clients</li>
</ul>

<div class="abs foot-h" style="left:695px;top:3545px">CONNECT</div>
<div class="abs foot-social" style="left:695px;top:3587px">
  <div><i></i>Friendwall</div><div><i></i>Chirper</div><div><i></i>Searchly</div><div><i></i>Worknet</div>
</div>

<div class="abs foot-h" style="left:892px;top:3545px">CONTACT INFO</div>
<div class="abs contact" style="left:892px;top:3587px">
  <div><i></i><span>Call Me<small>555-010-2244</small></span></div>
  <div><i></i><span>Message<small>hello@bytelantern.example</small></span></div>
  <div><i></i><span>Location<small>Lorem Ipsum is simply dummy text of the printing.</small></span></div>
</div>

<div class="abs" style="left:90px;top:3780px;width:1020px;height:1px;background:rgba(255,255,255,.2)"></div>
<div class="abs copy">Copy Right 2020-All Right Reserved.</div>

</body>
</html>
```